Halcyon 88/3 (plot no. 9 sector 67 Noida)

We need a brochure designed for our upcoming premium office complex located in Delhi NCR. The brochure is meant to be circulated to potential tenants and property consultants.The brochure should showcase key aspects of the office complex, showcasing it as a premium "Grade A" building which has multiple energy conservation concepts. Since the building has been awarded a "ZELQ Platinum Pre-certification", this should be highlighted. The brochure should include location details, key project specifications, and renderings of the project facade. The brochure should also showcase the strength of the project developer, by giving some history of the developer's past projects. All relevant details to be included in the brochure are attached.

Target Market(s)

Potential customers and real estate brokers for leasing the office space

Industry/Entity Type

Real Estate

Font styles to use
Sans Serif

Colors

Designer to choose colors to be used in the design.

Requirements
Must have
• Cover page, location map, design detailing and brief description as per the attached documents
• Being a platinum rated Green Building, green aspects should be highlighted
Nice to have
• Bright colors and textured background
Should not have
• black must be avoided

```html
<!DOCTYPE html>
<html lang="en">
<head>
<meta charset="utf-8">
<title>Halcyon 88/3 – Brochure Cover</title>
<link rel="stylesheet" href="https://fonts.googleapis.com/css2?family=Comfortaa:wght@300;400;600&display=swap">
<style>
  :root {
    --sky: #1e8cbd;
    --navy: #0f4f78;
    --brick: #c2444f;
    --olive: #b19b3f;
    --white: #ffffff;
  }
  html, body {
    margin: 0;
    padding: 0;
    width: 1200px;
    height: 849px;
    overflow: hidden;
    background: var(--white);
  }
  .cover {
    position: relative;
    width: 1200px;
    height: 849px;
    overflow: hidden;
    font-family: "Comfortaa", sans-serif;
    color: var(--white);
    background: linear-gradient(to bottom,
      var(--sky) 0, var(--sky) 506px,
      var(--navy) 506px, var(--navy) 623px,
      var(--brick) 623px, var(--brick) 730px,
      var(--olive) 730px, var(--olive) 849px);
  }
  .cover__edge {
    position: absolute;
    inset: 10px;
    border: 1px solid rgba(255,255,255,0.7);
  }
  .frame {
    position: absolute;
    inset: 0;
  }
  .project-render {
    position: absolute;
    left: 268px;
    top: 222px;
    width: 628px;
    height: 392px;
    background: linear-gradient(to bottom,
      #5aa9dc 0%, #8fc3e4 25%, #a79b8e 50%, #d68a3a 68%, #7d8f5a 88%, #4f6e3c 100%);
  }
  .rating {
    position: absolute;
    top: 74px;
    left: 0;
    width: 1200px;
    text-align: center;
    font-size: 22px;
    letter-spacing: 2px;
    line-height: 1;
  }
  .brand {
    position: absolute;
    top: 116px;
    left: 0;
    width: 1200px;
    text-align: center;
    margin: 0;
    font-weight: 400;
    font-size: 62px;
    line-height: 1;
    letter-spacing: 0;
  }
  .brand__tagline {
    position: absolute;
    top: 184px;
    left: 0;
    width: 1200px;
    text-align: center;
    margin: 0;
    font-weight: 400;
    font-size: 20.5px;
    line-height: 1;
    letter-spacing: 0.3px;
  }
  .headline {
    position: absolute;
    top: 654px;
    left: 0;
    width: 1200px;
    text-align: center;
    margin: 0;
    font-weight: 400;
    font-size: 46px;
    letter-spacing: 0.5px;
    line-height: 1;
  }
  .address {
    position: absolute;
    top: 776px;
    left: 0;
    width: 1200px;
    text-align: center;
    margin: 0;
    font-size: 20px;
    line-height: 1;
    font-weight: 400;
  }
</style>
</head>
<body>
  <main class="cover">
    <div class="cover__edge"></div>

    <div class="project-render" role="img" aria-label="Rendering of the Halcyon office building facade with coloured vertical fins, blue sky and landscaped frontage"></div>

    <svg class="frame" width="1200" height="849" viewBox="0 0 1200 849" aria-hidden="true">
      <polyline points="430,163 256,163 256,624 908,624 908,163 772,163"
                fill="none" stroke="#ffffff" stroke-width="5"/>
    </svg>

    <div class="rating" aria-label="Five star">★★★★★</div>
    <h1 class="brand">HALCYON</h1>
    <p class="brand__tagline">DEVELOPMENT AND CONSTRUCTION</p>

    <h2 class="headline">CREATING YOUR DREAM</h2>
    <p class="address">88/3 (plot no. 9 sector 67 Noida)</p>
  </main>
</body>
</html>
```